Automotive Retailer needs Branding HTML5 Ad Banners

Looking for a professional, polished set of graphic designs for use as digital ad banners. Don't know how to code? That's okay, we can also accept PDF or similar in a simple image set, and separately hire a coder to compile the slides into a banner. Preference would be for some sort of animation to catch and hold attention. Concepts to be designed around are below, please use company colours, which can be obtained by visiting our website www.brightlanemotorsales.com. Attached are images that can be used, and graphics can also be taken from our website as well.
a) Prairie Canada’s largest pre-owned dealership –200+ vehicles to choose from
b) Voted Canada’s Best Used Car Dealership 2021 & 2022 (can use the LotScore badges)
c) Winnipeg’s Best Deals on New & Used RV’s – Toy Haulers, Fifth Wheels, Bunkhouses, Couples coaches
d) Winnipeg’s Best Deals on New & Used RV’s – Payments starting at $99 b/w (plus tax, OAC)
e) Two Minutes from Hartvale @ Dunmore & Pellworth
f) Winnipeg’s most unique, most diverse pre-owned vehicle selection – 200+ to choose from
g) Other ideas?

```html
<!DOCTYPE html>
<html lang="en">
<head>
<meta charset="UTF-8">
<title>Brightlane Sales &amp; Finance – Winnipeg's Best Deals on RVs</title>
<link rel="stylesheet" href="https://fonts.googleapis.com/css2?family=Russo+One&display=swap">
<style>
  :root {
    --brand-red: #d7112a;
    --ink: #0d0d0d;
    --paper: #ffffff;
    --mist: #ececec;
    --frame-grey: #8a8a8a;
    --badge-gold: #d6a536;
    --sky-top: #4f8fd6;
    --sky-low: #b9d4ee;
    --ground: #a89c88;
  }
  html, body {
    margin: 0;
    padding: 0;
    width: 1200px;
    height: 1000px;
    overflow: hidden;
    background: var(--paper);
  }
  .banner {
    position: relative;
    width: 1200px;
    height: 1000px;
    overflow: hidden;
    background: var(--paper);
    font-family: "Russo One", "Arial Black", sans-serif;
  }
  .banner__backdrop {
    position: absolute;
    inset: 0;
    width: 1200px;
    height: 1000px;
  }
  .brand {
    position: absolute;
    left: 106px;
    top: 74px;
    color: var(--brand-red);
    font-size: 50px;
    line-height: 1;
    letter-spacing: 1px;
    text-transform: uppercase;
  }
  .brand__tagline {
    display: block;
    margin-top: 8px;
    margin-left: 150px;
    font-size: 26px;
    letter-spacing: 0.5px;
    text-transform: none;
  }
  .headline {
    position: absolute;
    left: 0;
    width: 1200px;
    top: 560px;
    margin: 0;
    text-align: center;
    color: var(--ink);
    font-size: 74px;
    line-height: 1;
    font-weight: 400;
    letter-spacing: 0;
    text-transform: uppercase;
  }
  .subhead {
    position: absolute;
    left: 0;
    width: 1200px;
    top: 652px;
    margin: 0;
    text-align: center;
    color: var(--brand-red);
    font-size: 44px;
    line-height: 1;
    font-weight: 400;
    text-transform: uppercase;
  }
  .rv-types {
    position: absolute;
    left: 90px;
    top: 755px;
    width: 1016px;
    display: grid;
    grid-template-columns: 486px 486px;
    grid-auto-rows: 84px;
    column-gap: 44px;
    row-gap: 25px;
    margin: 0;
    padding: 0;
    list-style: none;
  }
  .rv-types__item {
    display: flex;
    align-items: center;
    justify-content: center;
    background: var(--brand-red);
    border-radius: 8px;
    color: var(--paper);
    font-size: 28px;
    letter-spacing: 0.5px;
    text-transform: uppercase;
  }
  .ad-code {
    position: absolute;
    left: 1131px;
    top: 948px;
    color: var(--ink);
    font-size: 21px;
  }
</style>
</head>
<body>
  <main class="banner">
    <svg class="banner__backdrop" viewBox="0 0 625 520" preserveAspectRatio="none" aria-hidden="true">
      <defs>
        <linearGradient id="rv-photo-fill" x1="0" y1="0" x2="0" y2="1">
          <stop offset="0" stop-color="var(--sky-top)"/>
          <stop offset="0.45" stop-color="var(--sky-low)"/>
          <stop offset="0.62" stop-color="#e6e6e6"/>
          <stop offset="0.8" stop-color="#9a9a9a"/>
          <stop offset="1" stop-color="var(--ground)"/>
        </linearGradient>
      </defs>
      <circle class="corner-wash" cx="-110" cy="-60" r="315" fill="var(--mist)"/>
      <path class="accent-wedge" d="M292 0 L625 0 L625 150 Q570 230 505 282 Q490 292 478 280 L262 128 Q245 112 262 92 Z" fill="var(--brand-red)"/>
      <g class="award-badges">
        <circle cx="93" cy="180" r="36" fill="var(--badge-gold)"/>
        <circle cx="190" cy="180" r="36" fill="var(--badge-gold)"/>
        <circle cx="141" cy="182" r="42" fill="var(--badge-gold)" stroke="var(--paper)" stroke-width="3"/>
      </g>
    </svg>

    <svg class="banner__backdrop" viewBox="0 0 625 520" preserveAspectRatio="none">
      <path class="rv-photo" role="img" aria-label="Photo of a white travel trailer RV parked on a gravel lot under a blue sky"
        d="M332 0 L602 0 Q612 110 478 226 Q455 244 436 222 L322 62 Q302 22 332 0 Z"
        fill="url(#rv-photo-fill)" stroke="var(--frame-grey)" stroke-width="5"/>
    </svg>

    <div class="brand">Brightlane<span class="brand__tagline">Sales &amp; Finance</span></div>

    <h1 class="headline">Winnipeg's Best Deals</h1>
    <h2 class="subhead">On New &amp; Used RV's</h2>

    <ul class="rv-types">
      <li class="rv-types__item">Toy Haulers</li>
      <li class="rv-types__item">Fifth Wheels</li>
      <li class="rv-types__item">Bunkhouses</li>
      <li class="rv-types__item">Couples Coaches</li>
    </ul>

    <div class="ad-code">C54</div>
  </main>
</body>
</html>
```